Australian Meat, Seafood and Fresh Produce Website

Our organization is looking to design a simple, but eye catching website to show our services.
Our company exports West Australian FRESH fruit and vegetables, seafood and meat.
The website we are looking for would consist of:
- Landing Page
- Company info
- Directors bio
- Page that highlights our products
- Contact us page
We would like it to have a Chinese translated version as well.
Milo
Target Market(s)
Chinese Market
Industry/Entity Type
It Company
Number of Pages Required
1 page
Look and feel
Each slider illustrates characteristics of the customer's brand and the style your logo design should communicate.

```html
<!DOCTYPE html>
<html lang="en">
<head>
<meta charset="utf-8">
<title>Southgate Fresh Exports</title>
<link href="https://fonts.googleapis.com/css2?family=Lobster&family=Open+Sans:wght@400;600;700&display=swap" rel="stylesheet">
<style>
:root{
  --brown:#9a5a3c;
  --brown-dark:#6b3520;
  --cream:#f2ece8;
  --box:#f3ebe6;
  --input:#ecdcd5;
  --text:#555;
  --ink:#222;
  --white:#fff;
}
*{box-sizing:border-box;margin:0;padding:0}
html,body{width:1200px;height:2539px;overflow:hidden}
body{font-family:"Open Sans",sans-serif;color:var(--text);background:var(--white);position:relative}
section,header,footer{position:absolute;left:0;width:1200px}
.script{font-family:"Lobster",cursive;font-weight:400}
.wrap{position:absolute;left:183px;width:834px}

/* hero */
.hero{top:0;height:534px}
.hero-photo{position:absolute;inset:0;background:radial-gradient(ellipse at 50% 45%,#e0b6a4 0%,#c48e78 28%,#6a3a26 55%,#2a1610 80%,#140a06 100%)}
.brand{position:absolute;left:183px;top:24px;font-size:21px;color:var(--white);font-weight:400;letter-spacing:0.5px;white-space:nowrap}
.nav{position:absolute;right:183px;top:24px;display:flex;gap:36px}
.nav a{font-family:"Lobster",cursive;color:var(--white);text-decoration:none;font-size:17px}
.dots{position:absolute;top:494px;left:608px;display:flex;gap:4px}
.dots span{width:15px;height:15px;border-radius:50%;background:var(--white)}
.dots span.on{background:#bbb;border:4px solid var(--white)}

/* features */
.features{top:571px;height:209px}
.features .wrap{display:flex;gap:22px}
.feature{width:263px;height:209px;background:var(--box);border-top:5px solid var(--brown);text-align:center;padding-top:18px}
.feature svg{width:40px;height:40px}
.feature h3{font-size:20px;color:var(--brown);margin:6px 0 6px}
.feature p{font-size:10px;line-height:17px;color:var(--ink);padding:0 10px}
.btn{display:inline-block;background:var(--brown);color:var(--white);font-size:11px;font-weight:600;text-transform:uppercase;text-decoration:none}
.feature .btn{margin-top:14px;padding:7px 15px;font-size:10px}

/* welcome */
.welcome{top:819px;height:237px;background:var(--brown);color:var(--white);text-align:center}
.welcome h2{font-size:30px;margin-top:29px}
.welcome .lead{font-size:14px;margin-top:2px}
.welcome p.body{font-size:10.5px;line-height:19px;margin:20px auto 0;width:834px;text-align:left}
.btn-light{display:inline-block;background:var(--white);color:var(--brown);font-size:12px;font-weight:700;padding:10px 19px;margin-top:17px;text-decoration:none}

/* export */
.export{top:1056px;height:449px}
.export .col{position:absolute;left:183px;top:36px;width:402px}
h2.sec{font-size:28px;color:var(--brown)}
.sub{font-size:13px;color:#777;padding-bottom:10px;border-bottom:1px solid #ddd}
.product{padding:10px 0 12px;border-bottom:1px solid #ddd}
.product:last-of-type{border-bottom:none}
.product h4{font-size:18px;font-weight:400;color:var(--brown)}
.product h5{font-size:11px;font-weight:700;color:var(--ink);margin:2px 0 8px}
.product p{font-size:9.5px;line-height:17px;color:#666}
.export .btn{padding:11px 12px;font-size:12px;margin-top:6px}
.dish{position:absolute;left:615px;top:46px;width:585px;height:322px;background:radial-gradient(ellipse at 50% 50%,#e8a070 0%,#d26a3e 22%,#5f8e2e 45%,#9cc35e 60%,#f4f4f0 72%,#ffffff 100%)}

/* production */
.production{top:1505px;height:539px;background:var(--cream)}
.prod-col{position:absolute;left:183px;top:34px;width:478px}
.map{width:478px;height:265px;margin-top:22px;background:linear-gradient(180deg,#a8674a,#945538)}
.prod-col .note{font-size:10.5px;line-height:18px;color:var(--brown);margin-top:22px}
.btn-loc{display:inline-block;background:var(--brown);color:var(--white);font-size:14px;padding:9px 12px;border-radius:3px;margin-top:18px}
.news-col{position:absolute;left:683px;top:34px;width:337px}
.news{display:flex;gap:14px;padding:22px 0 12px;border-bottom:1px solid #ddd;height:103px}
.date{width:44px;text-align:center;color:var(--brown);line-height:1;flex:none}
.date b{display:block;font-size:40px;font-weight:400}
.date span{font-size:22px}
.news p{font-size:10px;line-height:18px;color:#666}
.news a{display:block;text-align:right;font-size:11px;font-weight:700;color:var(--brown);text-decoration:none;margin-top:4px}

/* contact */
.contact{top:2044px;height:246px}
.col3{position:absolute;top:38px;width:263px}
.col3 h3{font-size:21px;color:var(--brown);padding-bottom:6px;border-bottom:1px solid #ccc}
.c-row{display:flex;align-items:center;gap:10px;margin-top:8px;font-size:11px;color:var(--brown)}
.c-row:first-of-type{margin-top:18px}
.c-ico{width:39px;height:39px;border-radius:50%;background:var(--brown);display:flex;align-items:center;justify-content:center;flex:none}
.field{height:32px;background:var(--input);margin-top:8px;font-size:10px;color:#777;padding:9px 12px}
.field:first-of-type{margin-top:20px}
.sub-btn{display:inline-block;background:var(--brown);color:var(--white);font-size:12px;font-weight:700;padding:9px 15px;border-radius:3px;margin-top:10px}
.unsub{font-size:10px;color:var(--brown);margin-top:8px}
.why p{font-size:9.8px;line-height:16px;color:var(--ink);margin-top:16px}
.why .btn{padding:7px 15px;font-size:12px;border-radius:3px;margin-top:12px}

/* footer */
.footer{top:2290px;height:249px;background:var(--brown);text-align:center;color:var(--white)}
.footer h4{font-size:20px;font-weight:400;margin-top:54px}
.social{display:flex;justify-content:center;gap:8px;margin-top:14px}
.social span{width:38px;height:38px;border-radius:50%;background:var(--white);display:flex;align-items:center;justify-content:center}
.social span::after{content:"";width:9px;height:9px;border-radius:50%;background:var(--brown)}
.rule{width:34px;height:2px;background:var(--white);margin:24px auto 0}
.copy{font-size:10px;color:#e6cfc4;margin-top:20px}
</style>
</head>
<body>

<header class="hero">
  <div class="hero-photo" role="img" aria-label="Close-up photo of seasoned grilled fish fillet on a dark wooden board"></div>
  <div class="brand">SOUTHGATE FRESH EXPORTS</div>
  <nav class="nav"><a href="#">home</a><a href="#">about us</a><a href="#">our service</a><a href="#">our products</a><a href="#">contact us</a></nav>
  <div class="dots"><span></span><span class="on"></span><span></span></div>
</header>

<section class="features">
  <div class="wrap">
    <div class="feature">
      <svg viewBox="0 0 40 40" fill="#9a5a3c"><path d="M12 4h16v12a8 8 0 0 1-16 0z"/><path d="M12 7H6v4a6 6 0 0 0 6 6M28 7h6v4a6 6 0 0 1-6 6" fill="none" stroke="#9a5a3c" stroke-width="2.5"/><rect x="18" y="23" width="4" height="8"/><rect x="12" y="31" width="16" height="4"/></svg>
      <h3 class="script">Sucess Story</h3>
      <p>Lorem ipsum dolor sit amet, consectetur adipisicing elit, sed do eiusmod tempor incididunt aliqua.</p>
      <a class="btn" href="#">Read more</a>
    </div>
    <div class="feature">
      <svg viewBox="0 0 40 40" fill="#9a5a3c"><circle cx="20" cy="22" r="11"/><rect x="4" y="8" width="2.5" height="26"/><path d="M2 8v7h7V8" fill="none" stroke="#9a5a3c" stroke-width="2"/><path d="M35 8c-3 0-4 5-4 10h3v16h2.5V8z"/></svg>
      <h3 class="script">Our Services</h3>
      <p>Lorem ipsum dolor sit amet, consectetur adipisicing elit, sed do eiusmod tempor incididunt aliqua.</p>
      <a class="btn" href="#">Read more</a>
    </div>
    <div class="feature">
      <svg viewBox="0 0 40 40" fill="#9a5a3c"><path d="M20 2a12 12 0 0 0-12 12c0 9 12 22 12 22s12-13 12-22A12 12 0 0 0 20 2zm0 17a5 5 0 1 1 0-10 5 5 0 0 1 0 10z"/></svg>
      <h3 class="script">Location</h3>
      <p>Lorem ipsum dolor sit amet, consectetur adipisicing elit, sed do eiusmod tempor incididunt aliqua.</p>
      <a class="btn" href="#">Read more</a>
    </div>
  </div>
</section>

<section class="welcome">
  <h2 class="script">Welcome to our site!</h2>
  <p class="lead">Lorem ipsum dolor sit amet, consectetur adipisicing elit</p>
  <p class="body">Southgate Fresh Exports (SFE) aims to supply high quality West Australian produce to the rest of the World. Western Australia is known for its high quality farming practices and environment, which produces meat, seafood, fruit and vegetable of a caliber that is respected globally.</p>
  <a class="btn-light" href="#">READ MORE</a>
</section>

<section class="export">
  <div class="col">
    <h2 class="sec script">Export products list</h2>
    <p class="sub">Lorem ipsum dolor sit amet, consectetur adipisicing elit</p>
    <div class="product">
      <h4>Seafood</h4>
      <h5>Grain Fed (min 150 days)</h5>
      <p>150 day mid fed cattle with Marble Scores 1, 2, 3 that ensures you will have a grade of high quality beef to suit every sector of the market. Extremely well bred cattle of all breeds combined with a nutritional ration results in beef that delivers every time.</p>
    </div>
    <div class="product">
      <h4>Meat</h4>
      <h5>Grain Fed (min 150 days)</h5>
      <p>150 day mid fed cattle high quality Angus beef. Available in various marble scores this beef will simply deliver in all the areas that matter: texture, marbling, flavor and consistency. No doubt the best quality you can serve in markets where it matters. Medium to Long fed Angus bred cattle... it does not get any better. The choice of all the leading steak houses in Australia. Try it. Your customers will thank you for it.</p>
    </div>
    <a class="btn" href="#">View more products</a>
  </div>
  <div class="dish" role="img" aria-label="Photo of a prawn, olive and tomato salad on green leaves in a white bowl"></div>
</section>

<section class="production">
  <div class="prod-col">
    <h2 class="sec script">Production areas</h2>
    <p class="sub">Lorem ipsum dolor sit amet, consectetur adipisicing elit</p>
    <div class="map" role="img" aria-label="World map in brown showing production areas"></div>
    <p class="note">Lorem ipsum dolor sit amet, consectetur adipisicing elit Lorem ipsum dolor sit amet, consectetur adipisicing elit Lorem ipsum dolor sit amet, consectetur</p>
    <span class="btn-loc">Location details &raquo;</span>
  </div>
  <div class="news-col">
    <h2 class="sec script">Letest news &amp; events</h2>
    <p class="sub">Lorem ipsum dolor sid amet,</p>
    <div class="news"><div class="date"><b>01</b><span>JAN</span></div><div><p>Lorem Ipsum is that it has a more-or-less normal distribution of letters, as opposed to using 'Content here, content here', making it look like readable English.</p><a href="#">View More...</a></div></div>
    <div class="news"><div class="date"><b>20</b><span>MAY</span></div><div><p>Lorem Ipsum is that it has a more-or-less normal distribution of letters, as opposed to using 'Content here, content here', making it look like readable English.</p><a href="#">View More...</a></div></div>
    <div class="news"><div class="date"><b>14</b><span>JULY</span></div><div><p>Lorem Ipsum is that it has a more-or-less normal distribution of letters, as opposed to using 'Content here, content here', making it look like readable English.</p><a href="#">View More...</a></div></div>
  </div>
</section>

<section class="contact">
  <div class="col3" style="left:183px">
    <h3 class="script">Contact us</h3>
    <div class="c-row"><span class="c-ico"><svg width="14" height="14" viewBox="0 0 40 40" fill="#fff"><path d="M20 2a12 12 0 0 0-12 12c0 9 12 22 12 22s12-13 12-22A12 12 0 0 0 20 2zm0 17a5 5 0 1 1 0-10 5 5 0 0 1 0 10z"/></svg></span>1940 Quay Lane, Port Alma, WA, 6160</div>
    <div class="c-row"><span class="c-ico"><svg width="14" height="14" viewBox="0 0 24 24" fill="#fff"><path d="M6.6 10.8a15 15 0 0 0 6.6 6.6l2.2-2.2c.3-.3.7-.4 1-.2 1.1.4 2.3.6 3.6.6.6 0 1 .4 1 1V20c0 .6-.4 1-1 1A17 17 0 0 1 3 4c0-.6.4-1 1-1h3.5c.6 0 1 .4 1 1 0 1.3.2 2.5.6 3.6.1.3 0 .7-.2 1z"/></svg></span>+61 555 0142 &nbsp;&nbsp;/&nbsp;&nbsp; +61 555 0187</div>
    <div class="c-row"><span class="c-ico"><svg width="14" height="14" viewBox="0 0 24 24" fill="none" stroke="#fff" stroke-width="2"><rect x="3" y="5" width="18" height="14"/><path d="M3 5l9 8 9-8"/></svg></span>hello@southgatefresh.example</div>
  </div>
  <div class="col3" style="left:470px">
    <h3 class="script">News latter</h3>
    <div class="field">Enter Your Name</div>
    <div class="field">Enter Your Email Address</div>
    <span class="sub-btn">SUBCRIBE</span>
    <p class="unsub">Unsubscribe.!</p>
  </div>
  <div class="col3 why" style="left:754px">
    <h3 class="script">Why us</h3>
    <p>Lorem Ipsum is that it has a more-or-less normal distribution of letters, as opposed to using 'Content here, content here', making it look like readable English. Many desktop publishing packages and web page editors now use Lorem Ipsum as their default model text, and a search for 'lorem ipsum' will uncover many web sites still in their infancy.</p>
    <a class="btn" href="#">More</a>
  </div>
</section>

<footer class="footer">
  <h4>FOLLOW US</h4>
  <div class="social"><span></span><span></span><span></span><span></span><span></span></div>
  <div class="rule"></div>
  <p class="copy">&copy; Copyright 2015 Southgate Fresh Exports . All Rights Reserved.</p>
</footer>

</body>
</html>
```